MORVEK IT Limited Buisness card logo

I am setting up a IT Consultancy company and want a logo that is related to the IT industry, but also i am thinking that the A in MOR and the A in VEK are linked together maybe horizontally and vertically, also thought about the A being @ as it symbolises IT services. This logo will be used on paperwork, business cards and website.

Industry/Entity Type

Business

Contact Information for Business Card

Gareth Wilmslow
MORVEK IT Limited
IT Consultant
Mobile: 07912563084
Email: garethwk@fernmail.co.uk

Requirements
Must have
• IT Theme

```html
<!DOCTYPE html>
<html lang="en">
<head>
<meta charset="utf-8">
<title>MORVEK IT Ltd – Business Card</title>
<link rel="stylesheet" href="https://fonts.googleapis.com/css2?family=Open+Sans:wght@400;700&display=swap">
<style>
  :root {
    --brand-red: #8b0000;
    --paper: #ffffff;
    --faint-red: #cc8585;
  }
  html, body {
    margin: 0;
    padding: 0;
    overflow: hidden;
    background: var(--paper);
  }
  .card {
    position: relative;
    width: 1200px;
    height: 686px;
    overflow: hidden;
    font-family: "Open Sans", Arial, sans-serif;
    color: var(--brand-red);
    background: var(--paper);
  }
  .card-backdrop {
    position: absolute;
    inset: 0;
  }
  .company-title {
    position: absolute;
    top: 0;
    left: 0;
    width: 1130px;
    height: 126px;
    margin: 0;
    display: flex;
    align-items: center;
    justify-content: center;
    color: var(--paper);
    font-size: 52px;
    font-weight: 700;
    letter-spacing: 0.5px;
  }
  .brand-mark {
    position: absolute;
    left: 63px;
    top: 214px;
    font-size: 29px;
    font-weight: 700;
    line-height: 1;
  }
  .role-title {
    position: absolute;
    left: 218px;
    top: 212px;
    margin: 0;
    font-size: 41px;
    font-weight: 700;
    line-height: 1;
  }
  .divider {
    position: absolute;
    left: 569px;
    top: 167px;
    width: 1px;
    height: 215px;
    background: var(--brand-red);
  }
  .contact-name {
    position: absolute;
    left: 684px;
    top: 178px;
    margin: 0;
    font-size: 36px;
    font-weight: 700;
    line-height: 1;
  }
  .contact-line {
    position: absolute;
    left: 678px;
    display: flex;
    align-items: center;
    font-size: 36px;
    font-weight: 400;
    line-height: 1;
  }
  .contact-line svg {
    flex: none;
    fill: var(--brand-red);
  }
  .contact-phone { top: 228px; }
  .contact-phone .value { margin-left: 10px; }
  .contact-email { top: 277px; }
  .contact-email .value { margin-left: 18px; }
  .brand-mark-faint {
    position: absolute;
    left: 960px;
    top: 535px;
    font-size: 34px;
    font-weight: 700;
    line-height: 1;
    color: var(--faint-red);
  }
</style>
</head>
<body>
<div class="card">
  <svg class="card-backdrop" width="1200" height="686" viewBox="0 0 1200 686" aria-hidden="true">
    <rect x="0" y="0" width="1200" height="126" fill="var(--brand-red)"/>
    <rect x="0" y="425" width="1200" height="261" fill="var(--brand-red)"/>
    <ellipse cx="1175" cy="590" rx="337" ry="165" fill="var(--paper)"/>
  </svg>

  <h1 class="company-title">MORVEK IT LTD</h1>

  <div class="brand-mark">MORVEK</div>
  <p class="role-title">IT Consultant</p>

  <div class="divider"></div>

  <h2 class="contact-name">Gareth Wilmslow</h2>

  <div class="contact-line contact-phone">
    <svg width="16" height="32" viewBox="0 0 16 32" aria-hidden="true">
      <rect x="1" y="4" width="14" height="27" rx="2"/>
      <rect x="10" y="0" width="2" height="5"/>
      <rect x="3.5" y="7" width="9" height="7" fill="var(--paper)"/>
      <rect x="3.5" y="17" width="2.5" height="2" fill="var(--paper)"/>
      <rect x="7" y="17" width="2.5" height="2" fill="var(--paper)"/>
      <rect x="10.5" y="17" width="2.5" height="2" fill="var(--paper)"/>
      <rect x="3.5" y="21" width="2.5" height="2" fill="var(--paper)"/>
      <rect x="7" y="21" width="2.5" height="2" fill="var(--paper)"/>
      <rect x="10.5" y="21" width="2.5" height="2" fill="var(--paper)"/>
      <rect x="3.5" y="25" width="2.5" height="2" fill="var(--paper)"/>
      <rect x="7" y="25" width="2.5" height="2" fill="var(--paper)"/>
      <rect x="10.5" y="25" width="2.5" height="2" fill="var(--paper)"/>
    </svg>
    <span class="value">- 07912563084</span>
  </div>

  <div class="contact-line contact-email">
    <svg width="34" height="20" viewBox="0 0 34 20" aria-hidden="true">
      <rect x="0" y="0" width="34" height="20"/>
      <polyline points="1,1 17,12 33,1" fill="none" stroke="var(--paper)" stroke-width="2"/>
      <polyline points="1,19 12,9 M33,19 22,9" fill="none" stroke="var(--paper)" stroke-width="1.5"/>
    </svg>
    <span class="value">garethwk@fernmail.co.uk</span>
  </div>

  <div class="brand-mark-faint">MORVEK</div>
</div>
</body>
</html>
```